My company is all about art and painting people's walls, cars and everything you can imagine, I would like a sharp professional buisness card which still has a good creative element

Industry/Entity Type

Painting

Contact Information for Business Card

Ve Rubel Art
Canvass,Murals,Vehicles,Cover art and tattoo design
Commissions available..
Www.brightwall.example/tavmiu

```html
<!DOCTYPE html>
<html lang="en">
<head>
<meta charset="utf-8">
<title>Ve Rubel Art — Business Card</title>
<link rel="stylesheet" href="https://fonts.googleapis.com/css2?family=Merriweather:wght@700;900&family=Merriweather+Sans:wght@800&display=swap">
<style>
  :root {
    --card-black: #000000;
    --text-white: #ffffff;
    --text-outline: #1f6f68;
    --paint-lilac: #b9aee6;
    --paint-cream: #f3ecd9;
    --paint-pink: #d9479c;
    --paint-teal: #4fb0a8;
  }
  * { margin: 0; padding: 0; box-sizing: border-box; }
  html, body {
    width: 1200px;
    height: 693px;
    overflow: hidden;
    background: var(--card-black);
  }
  .card {
    position: relative;
    width: 1200px;
    height: 693px;
    display: flex;
    background: var(--card-black);
  }
  .artwork-panel {
    width: 498px;
    height: 693px;
    flex: none;
    background:
      radial-gradient(ellipse 45% 55% at 50% 30%, rgba(217,71,156,0.55), transparent 70%),
      radial-gradient(ellipse 30% 40% at 70% 60%, rgba(79,176,168,0.35), transparent 70%),
      linear-gradient(120deg, var(--paint-lilac) 0%, var(--paint-cream) 45%, var(--paint-lilac) 100%);
  }
  .card-info {
    flex: 1;
    display: flex;
    flex-direction: column;
    align-items: center;
    text-align: center;
    color: var(--text-white);
    font-family: "Merriweather", Georgia, serif;
    -webkit-text-stroke: 2px var(--text-outline);
    paint-order: stroke fill;
  }
  .brand-name {
    margin-top: 30px;
    font-size: 92px;
    font-weight: 900;
    letter-spacing: 1px;
    line-height: 1.1;
  }
  .services {
    margin-top: 42px;
    font-family: "Merriweather Sans", Arial, sans-serif;
    font-size: 42px;
    font-weight: 800;
    line-height: 1.3;
  }
  .commissions {
    margin-top: 44px;
    font-family: "Merriweather Sans", Arial, sans-serif;
    font-size: 42px;
    font-weight: 800;
  }
  .web-address {
    margin-top: 42px;
    font-size: 34px;
    font-weight: 900;
  }
</style>
</head>
<body>
  <div class="card">
    <div class="artwork-panel" role="img" aria-label="Expressive painted portrait in lilac, pink and teal brushstrokes"></div>
    <div class="card-info">
      <h1 class="brand-name">Ve Rubel Art</h1>
      <p class="services">Canvasses, Murals,<br>Vehicles, Cover Art, &amp;<br>Tattoo Design</p>
      <p class="commissions">Commissions Available</p>
      <p class="web-address">www.brightwall.example/tavmiu</p>
    </div>
  </div>
</body>
</html>
```